Annual review for The Heron Collective

The Heron Collective is a small public relations agency in London specialising in corporate and public affairs. Most of our work is international and we have a strong connection to South Africa. We would like to prepare a short annual review for 2016. The review will serve as both a review of our activities in 2016, and as a credentials document. Content then will include:
1. An introduction to the business
2. Who we are
3. Projects and clients undertaken in 2016
4. News and views
We imagine it will be used mostly as a pdf but would like it to be suitable for print. We envisage it to be about 8 pages long. The design look and feel should convey a business, while small, of stature. We shall include some of our client logos but we would welcome the use of some photography / imagery to have visual impact (although we don't have very much of our own!). The corporate look and feel is white, grey and black.

Industry/Entity Type

Public Relation

Font styles to use
Sans Serif

Requirements
Must have
• My project must convey a business with flair and gravitas, that punches above its weight.
Nice to have
• Thoughtful use of imagery.

```html
<!DOCTYPE html>
<html lang="en">
<head>
<meta charset="utf-8">
<title>The Heron Collective — Annual Review Cover</title>
<link rel="stylesheet" href="https://fonts.googleapis.com/css2?family=Montserrat:wght@600&family=Open+Sans:wght@400&display=swap">
<style>
  :root {
    --backdrop: #bdbdbd;
    --slate: #4a4d54;
    --rule: #2e2727;
    --paper: #e4e4e4;
    --ink: #3f4248;
    --white: #ffffff;
    --fold: rgba(0,0,0,0.08);
    --haze: #b9b9b9;
    --sea: #7a7a7a;
    --sea-deep: #555555;
    --land: #2b2b2b;
    --surf: rgba(245,245,245,0.7);
  }
  html, body {
    margin: 0;
    width: 1200px;
    height: 800px;
    overflow: hidden;
    background: var(--backdrop);
  }
  .spread {
    position: absolute;
    left: 60px;
    top: 40px;
    width: 1080px;
    height: 720px;
    display: flex;
    flex-direction: column;
    background: var(--paper);
    box-shadow: 0 6px 18px rgba(0,0,0,0.18);
  }
  .band-top {
    height: 200px;
    background: var(--slate);
    position: relative;
  }
  .rule {
    height: 7px;
    background: var(--rule);
  }
  .photo-band {
    height: 320px;
    background:
      radial-gradient(ellipse 22% 16% at 54% 86%, var(--surf) 0%, rgba(245,245,245,0) 100%),
      radial-gradient(ellipse 14% 10% at 44% 58%, rgba(230,230,230,0.45) 0%, rgba(230,230,230,0) 100%),
      radial-gradient(ellipse 48% 60% at 82% 72%, rgba(30,30,30,0.85) 0%, rgba(30,30,30,0.55) 45%, rgba(30,30,30,0) 100%),
      radial-gradient(ellipse 40% 30% at 70% 8%, rgba(210,210,210,0.6) 0%, rgba(210,210,210,0) 100%),
      radial-gradient(ellipse 60% 70% at 0% 100%, rgba(40,40,40,0.55) 0%, rgba(40,40,40,0) 100%),
      linear-gradient(180deg, var(--haze) 0%, #9c9c9c 14%, var(--sea) 40%, #6a6a6a 70%, var(--sea-deep) 100%);
  }
  .band-bottom {
    flex: 1;
    position: relative;
    background: linear-gradient(90deg, #ededed 0%, #e3e3e3 50%, #dedede 100%);
  }
  .fold {
    position: absolute;
    top: 0;
    bottom: 0;
    left: 540px;
    width: 2px;
    background: var(--fold);
  }
  .brand {
    display: flex;
    align-items: center;
    gap: 12px;
    font-family: "Montserrat", sans-serif;
    font-weight: 600;
  }
  .brand-dot {
    border-radius: 50%;
    box-sizing: border-box;
  }
  .cover-brand {
    position: absolute;
    left: 640px;
    bottom: 28px;
    color: var(--white);
    font-size: 26px;
  }
  .cover-brand .brand-dot {
    width: 30px;
    height: 30px;
    border: 2px solid var(--white);
  }
  .tagline {
    position: absolute;
    left: 600px;
    width: 420px;
    top: 62px;
    margin: 0;
    text-align: center;
    font-family: "Open Sans", sans-serif;
    font-size: 15px;
    line-height: 1.35;
    color: var(--ink);
  }
  .back-contact {
    position: absolute;
    left: 150px;
    top: 50px;
    color: var(--ink);
  }
  .back-contact .brand {
    font-size: 21px;
  }
  .back-contact .brand-dot {
    width: 24px;
    height: 24px;
    border: 2px solid var(--ink);
  }
  .address {
    margin: 2px 0 0 36px;
    font-family: "Open Sans", sans-serif;
    font-style: normal;
    font-size: 14px;
    line-height: 1.3;
  }
</style>
</head>
<body>
  <div class="spread">
    <div class="band-top">
      <div class="cover-brand brand">
        <span class="brand-dot"></span>
        <span class="brand-name">The Heron Collective</span>
      </div>
    </div>
    <div class="rule"></div>
    <div class="photo-band" role="img" aria-label="Black and white aerial photograph of a rocky cape headland jutting into the sea, with white surf breaking along the shore and hazy coastline in the distance"></div>
    <div class="rule"></div>
    <div class="band-bottom">
      <div class="back-contact">
        <div class="brand">
          <span class="brand-dot"></span>
          <span class="brand-name">The Heron Collective</span>
        </div>
        <address class="address">
          42 Marlow Lane, London EC1A 2BX<br>
          11 rue des Lilas, 75011 Paris<br>
          hello@heroncollective.com
        </address>
      </div>
      <p class="tagline">We provide corporate and public affairs consultancy advice as well as corporate responsibility and sustainable development policy expertise.</p>
    </div>
    <div class="fold"></div>
  </div>
</body>
</html>
```